Business Cards, Letterhead, Corporate Materials

Harlow Building Partners, Inc. needs brand identity and marketing materials.

Target Market(s)

Home Owners, Architects, Engineers.

Contact Information for Business Card

Business Cards for myself the President

Font styles to use
Serif

Colors
3377b5
0255a3
cfdfed
cee9f5
86cae7
0393ce
000000
ffffff
f5f5f5

Requirements
Must have
• My name, my address, my email, phone number, company logo, my title. my contractor's license number, web address.
Nice to have
• Very clean professional modern business cards for company president.

```html
<!DOCTYPE html>
<html lang="en">
<head>
<meta charset="utf-8">
<title>Harlow Building Partners, Inc. — Business Card</title>
<link rel="stylesheet" href="https://fonts.googleapis.com/css2?family=Source+Serif+4:wght@400;700&display=swap">
<style>
  :root {
    --navy: #143566;
    --blue-deep: #0255a3;
    --blue-mid: #3377b5;
    --teal: #2a86a8;
    --ink: #1a1a1a;
    --name-ink: #333333;
    --grey-logo: #e4e6ea;
    --paper: #ffffff;
    --paper-shade: #e9e9eb;
    --stage: #f5f5f5;
  }
  * { margin: 0; padding: 0; box-sizing: border-box; }
  html, body { width: 1200px; height: 800px; overflow: hidden; }
  body {
    background: var(--stage);
    font-family: "Source Serif 4", Georgia, serif;
    position: relative;
  }
  .card {
    position: absolute;
    top: 245px;
    width: 540px;
    height: 309px;
    box-shadow: 0 10px 28px rgba(0,0,0,0.18);
    overflow: hidden;
  }
  /* Front */
  .card-front {
    left: 40px;
    background: linear-gradient(155deg, var(--navy) 0%, var(--blue-deep) 45%, var(--teal) 100%);
    display: flex;
    align-items: center;
    justify-content: center;
  }
  .brand {
    display: flex;
    align-items: center;
    gap: 14px;
  }
  .brand-mark {
    width: 44px;
    height: 44px;
    flex: none;
    background: var(--grey-logo);
  }
  .brand-name {
    font-size: 23px;
    font-weight: 400;
    line-height: 1.15;
    letter-spacing: 1px;
    color: var(--grey-logo);
    text-transform: uppercase;
  }
  /* Back */
  .card-back {
    left: 620px;
    background: linear-gradient(135deg, var(--paper) 0%, var(--paper) 45%, var(--paper-shade) 100%);
  }
  .card-back .brand {
    position: absolute;
    left: 34px;
    top: 120px;
    gap: 10px;
  }
  .card-back .brand-mark {
    width: 30px;
    height: 30px;
    background: var(--blue-deep);
  }
  .card-back .brand-name {
    font-size: 15px;
    color: var(--blue-deep);
    letter-spacing: 0.6px;
  }
  .person {
    position: absolute;
    left: 34px;
    top: 210px;
    font-weight: 700;
    text-transform: uppercase;
  }
  .person-name { font-size: 20px; color: var(--name-ink); letter-spacing: 0.6px; line-height: 1.2; }
  .person-title { font-size: 14px; color: var(--blue-mid); letter-spacing: 0.9px; margin-top: 2px; }
  .details {
    position: absolute;
    left: 296px;
    top: 40px;
    right: 20px;
    color: var(--ink);
    font-size: 14px;
    line-height: 1.45;
  }
  .license { color: var(--blue-mid); margin-bottom: 44px; }
  .address { margin-bottom: 2px; }
  .contact-line { display: flex; align-items: center; gap: 8px; }
  .contact-line svg { width: 14px; height: 14px; flex: none; }
  .plain-line { padding-left: 22px; }
</style>
</head>
<body>
  <section class="card card-front" aria-label="Business card front">
    <div class="brand">
      <span class="brand-mark" aria-hidden="true"></span>
      <span class="brand-name">Harlow Building<br>Partners, Inc.</span>
    </div>
  </section>

  <section class="card card-back" aria-label="Business card back">
    <div class="brand">
      <span class="brand-mark" aria-hidden="true"></span>
      <span class="brand-name">Harlow Building<br>Partners, Inc.</span>
    </div>
    <div class="person">
      <p class="person-name">Daniel Reyes</p>
      <p class="person-title">President</p>
    </div>
    <div class="details">
      <p class="license">License No.:71846025</p>
      <p class="address">118, Cedar Court<br>Maple Avenue, CA 35102</p>
      <p class="contact-line">
        <svg viewBox="0 0 14 14" aria-hidden="true"><rect x="3" y="1" width="8" height="12" rx="1.5" fill="none" stroke="#0255a3" stroke-width="1.6"/><rect x="5.5" y="10" width="3" height="1.3" fill="#0255a3"/></svg>
        415 . 582 . 7309
      </p>
      <p class="contact-line">
        <svg viewBox="0 0 14 14" aria-hidden="true"><rect x="1" y="3" width="12" height="9" fill="#0255a3"/><path d="M1 3 L7 8 L13 3" fill="none" stroke="#ffffff" stroke-width="1.2"/></svg>
        info@HarlowBuilding.com
      </p>
      <p class="plain-line">www.HarlowBuilding.com</p>
    </div>
  </section>
</body>
</html>
```